Business Card for Makeup Artist

I need a business card designed for my makeup and hair artistry business which is primarily events and weddings focused. The card needs to be sleek, simple, stylish and appealing to women. I would prefer a white background but open to suggestions also. I also love the marble background look. I have attached some example pics. It needs to be a double sided card with logo and/or design on one side and contact details in the centre of the card on the other side. NO LOGO ON BACK. Examples attached.

Target Market(s)

Females age 14-55

Industry/Entity Type

Business

Contact Information for Business Card

Nora Vint
Principal Makeup Artist
P: 0413 925 214
E: nora@lumirabeauty.com.au
W: www.lumirabeauty.com.au

Requirements
Should not have
• No yellow, green, red or blue in the design.

```html
<!DOCTYPE html>
<html lang="en">
<head>
<meta charset="utf-8">
<title>Lumira Makeup Artistry — Business Card</title>
<link rel="stylesheet" href="https://fonts.googleapis.com/css2?family=Raleway:wght@400;600&family=Roboto+Condensed:wght@400&display=swap">
<style>
  :root {
    --stage: #e9e6e3;
    --card-white: #ffffff;
    --card-black: #141414;
    --card-black-edge: #0b0b0b;
    --ink-grey: #6e6f72;
    --ink-white: #f4f4f4;
    --accent-pink: #d9559f;
  }
  * { box-sizing: border-box; margin: 0; padding: 0; }
  html, body {
    width: 1200px;
    height: 1200px;
    overflow: hidden;
    background: var(--stage);
  }
  .canvas {
    width: 1200px;
    height: 1200px;
    display: flex;
    flex-direction: column;
    align-items: center;
    justify-content: center;
    gap: 60px;
  }
  .card {
    position: relative;
    width: 860px;
    height: 491px;
    border-radius: 30px;
    overflow: hidden;
    box-shadow: 0 6px 22px rgba(0, 0, 0, 0.14);
  }

  /* Front */
  .card--front { background: var(--card-white); }
  .brand {
    position: absolute;
    left: 0; right: 0;
    top: 150px;
    text-align: center;
  }
  .brand__name {
    font-family: "Raleway", sans-serif;
    font-weight: 400;
    font-size: 66px;
    letter-spacing: 4px;
    color: var(--ink-grey);
    line-height: 1.1;
  }
  .brand__tag {
    margin-top: 6px;
    font-family: "Raleway", sans-serif;
    font-weight: 400;
    font-size: 34px;
    letter-spacing: 2px;
    color: var(--ink-grey);
  }
  .front__url {
    position: absolute;
    left: 0; right: 0;
    bottom: 66px;
    text-align: center;
    font-family: "Roboto Condensed", sans-serif;
    font-size: 19px;
    color: var(--accent-pink);
  }

  /* Back */
  .card--back {
    background: radial-gradient(ellipse at 60% 35%, #222 0%, var(--card-black) 55%, var(--card-black-edge) 100%);
    display: flex;
    align-items: center;
    justify-content: center;
  }
  .details {
    display: flex;
    flex-direction: column;
    align-items: flex-start;
  }
  .person {
    position: relative;
  }
  .person__accent {
    position: absolute;
    left: -40px;
    top: 50px;
    width: 22px;
    height: 52px;
    background: var(--accent-pink);
  }
  .person__name {
    font-family: "Raleway", sans-serif;
    font-weight: 600;
    font-size: 44px;
    letter-spacing: 1px;
    color: var(--ink-white);
    text-transform: uppercase;
    line-height: 1;
  }
  .person__role {
    margin-top: 8px;
    font-family: "Roboto Condensed", sans-serif;
    font-size: 22px;
    letter-spacing: 0.5px;
    color: var(--accent-pink);
    text-transform: uppercase;
  }
  .contact {
    margin-top: 36px;
    padding-left: 24px;
    list-style: none;
    font-family: "Roboto Condensed", sans-serif;
    font-size: 21px;
    line-height: 1.45;
    color: var(--ink-white);
  }
</style>
</head>
<body>
  <main class="canvas">
    <section class="card card--front" aria-label="Card front">
      <div class="brand">
        <p class="brand__name">Lumira</p>
        <p class="brand__tag">MAKEUP ARTISTRY</p>
      </div>
      <p class="front__url">www.lumirabeauty.com.au</p>
    </section>

    <section class="card card--back" aria-label="Card back">
      <div class="details">
        <div class="person">
          <div class="person__accent"></div>
          <h1 class="person__name">Nora Vint</h1>
          <p class="person__role">Principal Makeup Artist</p>
        </div>
        <ul class="contact">
          <li>P: 0413 925 214</li>
          <li>E: nora@lumirabeauty.com.au</li>
          <li>W: www.lumirabeauty.com.au</li>
        </ul>
      </div>
    </section>
  </main>
</body>
</html>
```